Can you make our site AWESOME?

Hi Guys,

I am a co-founder of Tumble Crate Rentals Oz, the world's first e-commerce skip bin business.

We are looking to update our site before a launch into the UK in March.

Please help us by submitting your designs for the following pages:

- Home page (www.tumblecraterentalsoz.example.au)
- About us (https://www.tumblecraterentalsoz.example.au/pages/about-us
- Contact us (https://www.tumblecraterentalsoz.example.au/pages/contact-us)
- Quick Quote / Pricing (https://www.tumblecraterentalsoz.example.au/pages/free-instant-quote-skip-bin-hire)

NOTES:
- Design should be high-converting
- best designs will be fresh, modern, easy to read, distinctive and memorable
- please use our logo and video colours
- feel free to change logos, layout, images and anything else you feel can be improved
- the winning designer will potentially have the opportunity to re-design the other pages on our site
- brief is for design only

Any questions just ask.

Thanks,
Morton

```html
<!DOCTYPE html>
<html lang="en">
<head>
<meta charset="utf-8">
<title>Tumble Crate Rentals Oz — Home</title>
<link href="https://fonts.googleapis.com/css2?family=Ubuntu:wght@400;500;700&family=Open+Sans:wght@400;600;700&display=swap" rel="stylesheet">
<style>
:root{
  --navy:#17137a;
  --purple:#2c1ab0;
  --deep:#120f5e;
  --teal:#0f8a6e;
  --teal-dark:#0b5f62;
  --yellow:#f6c500;
  --green:#0c9a5b;
  --ink:#1d1b4f;
  --grey:#8a8aa0;
  --light:#e6e6ee;
  --white:#ffffff;
}
*{box-sizing:border-box;margin:0;padding:0}
html,body{width:1200px;height:3448px;overflow:hidden;background:var(--white)}
body{font-family:"Open Sans",Arial,sans-serif;color:var(--ink)}
.page{position:relative;width:1200px;height:3448px;overflow:hidden}
.abs{position:absolute}
h1,h2,h3,.brand{font-family:"Ubuntu",Arial,sans-serif}

/* nav */
.nav{left:0;top:0;width:790px;height:64px;background:var(--white);clip-path:polygon(0 0,100% 0,97% 100%,0 100%);z-index:5}
.brand{position:absolute;left:20px;top:17px;font-weight:700;font-size:12px;line-height:14px;color:var(--navy);letter-spacing:.3px;white-space:nowrap}
.nav-link{position:absolute;top:25px;font-size:11px;letter-spacing:1.5px;color:var(--ink);font-weight:600;white-space:nowrap}
.account{right:42px;top:22px;display:flex;gap:30px;font-size:11px;letter-spacing:1px;color:#b5b5c2;z-index:5;white-space:nowrap}

/* hero */
.hero-bg{left:0;top:0;width:1200px;height:593px}
.eyebrow{font-size:10px;font-weight:700;letter-spacing:1.5px;color:var(--yellow);display:flex;align-items:center;gap:10px;white-space:nowrap}
.eyebrow .num{color:var(--grey);font-weight:400}
.eyebrow .rule{width:70px;height:1px;background:var(--grey);opacity:.6}
.hero-eyebrow{left:99px;top:200px}
.hero-title{left:99px;top:224px;font-size:31px;font-weight:700;color:var(--white);white-space:nowrap}
.search{display:flex;height:42px}
.search .field{flex:1;background:rgba(10,10,80,.75);color:#c9c9e6;font-size:14px;font-style:italic;display:flex;align-items:center;padding-left:14px}
.search .btn{width:110px;background:var(--yellow);color:var(--white);font-weight:700;font-size:14px;display:flex;align-items:center;justify-content:center;clip-path:polygon(0 0,100% 0,90% 100%,0 100%)}
.hero-search{left:87px;top:340px;width:488px}
.audience{font-family:"Ubuntu",Arial,sans-serif;font-size:15px;color:#c5c5d0;display:flex;align-items:center;gap:10px;white-space:nowrap}
.audience::before{content:"★";color:var(--yellow);font-size:13px}

/* sections */
.section-eyebrow .num{color:#b8b8c8}
.section-title{font-size:28px;font-weight:700;color:var(--navy);white-space:nowrap}
.band{left:0;top:1095px;width:1200px;height:586px;background:linear-gradient(160deg,#0d6e6a 0%,#155a86 45%,#2417a6 100%)}
.card{top:835px;width:288px;height:361px;background:var(--white);box-shadow:0 10px 30px rgba(20,20,80,.15);text-align:center;padding:60px 24px 0;z-index:2}
.card .art{width:180px;height:160px;margin:0 auto 32px;background:linear-gradient(150deg,var(--teal),var(--purple));clip-path:polygon(30% 0,70% 0,100% 30%,100% 70%,70% 100%,30% 100%,0 70%,0 30%);opacity:.9}
.card h3{font-size:13px;font-weight:700;margin-bottom:12px;color:var(--ink)}
.card p{font-size:11.5px;line-height:17px;color:#55556a}

.reviews-title{color:var(--white)}
.arrow{top:1310px;width:34px;height:30px;border:1.5px solid #7fd4ee;color:#bfefff;font-size:17px;display:flex;align-items:center;justify-content:center}
.dots{left:1101px;top:1321px;display:flex;gap:6px}
.dots i{width:5px;height:5px;border-radius:50%;background:rgba(255,255,255,.45)}
.dots i:first-child{background:var(--white)}
.review{top:1410px;width:345px;height:156px;background:var(--white);clip-path:polygon(0 0,90% 0,100% 18%,100% 100%,0 100%);padding:22px 26px 0 14px}
.review .quote{position:absolute;left:14px;top:0;font-family:"Ubuntu",Arial,sans-serif;font-size:110px;line-height:110px;color:#ececf2}
.review .head{position:relative;display:flex;align-items:center;font-size:10px;white-space:nowrap}
.review .name{font-weight:700;color:var(--ink);margin-right:8px}
.review .date{color:var(--grey)}
.review .stars{margin-left:auto;color:var(--yellow);font-size:17px;letter-spacing:3px}
.review p{position:relative;margin:6px 0 0 36px;font-size:11.5px;line-height:18px;color:#2d2d45}

/* features */
.feature h3{font-size:13px;font-weight:700;margin-bottom:8px;color:var(--ink);white-space:nowrap}
.feature p{font-size:11.5px;line-height:20px;color:#55556a}

/* ready */
.map{left:299px;top:2594px;width:563px;height:511px;border-radius:38% 46% 42% 30%/34% 40% 48% 44%;background:linear-gradient(170deg,#139b78 0%,#1a5f8e 45%,#2a17ac 100%);box-shadow:0 0 60px rgba(90,60,230,.45)}
.ready-eyebrow{left:0;width:1200px;top:2760px;text-align:center;font-size:10px;font-weight:700;letter-spacing:1.8px;color:var(--yellow)}
.ready-title{left:0;width:1200px;top:2781px;text-align:center;font-size:29px;font-weight:700;color:var(--white)}
.ready-search{left:345px;top:2847px;width:483px}

/* footer */
.footer{left:0;top:3140px;width:1200px;height:308px;background:var(--deep);color:var(--white)}
.foot-col{top:55px}
.foot-col h4{font-size:12px;font-weight:700;margin-bottom:14px;white-space:nowrap}
.foot-col li{list-style:none;font-size:12px;line-height:20px;color:#d6d6ea}
.foot-col p{font-size:12px;line-height:18px;color:#d6d6ea;width:260px}
.subscribe{left:697px;top:130px;display:flex;height:42px}
.subscribe .field{width:216px;border-bottom:1px solid #5a58a8;font-size:13px;font-style:italic;color:#c9c9e6;display:flex;align-items:center;padding-left:4px}
.subscribe .btn{width:124px;background:var(--green);font-size:13px;font-weight:600;display:flex;align-items:center;justify-content:center;clip-path:polygon(0 0,100% 0,92% 100%,0 100%)}
.copyright{left:87px;top:263px;font-size:11px;color:#d6d6ea}
</style>
</head>
<body>
<div class="page">

  <!-- hero -->
  <svg class="abs hero-bg" viewBox="0 0 1200 593" role="img" aria-label="Skip bins stacked in a yard, tinted blue and green">
    <defs>
      <linearGradient id="heroGrad" x1="0" y1="0" x2="1" y2="1">
        <stop offset="0" stop-color="#0c5e6e"/>
        <stop offset=".45" stop-color="#1a3a92"/>
        <stop offset="1" stop-color="#2617a8"/>
      </linearGradient>
    </defs>
    <polygon points="0,0 970,0 621,593 0,593" fill="url(#heroGrad)"/>
    <polygon points="420,0 970,0 621,593 300,593" fill="#1fae8a" opacity=".18"/>
  </svg>

  <nav class="abs nav">
    <div class="brand">Tumble Crate<br>Rentals Oz</div>
    <span class="nav-link" style="left:147px">PRICING</span>
    <span class="nav-link" style="left:265px">LEARN MORE</span>
    <span class="nav-link" style="left:417px">ABOUT</span>
    <span class="nav-link" style="left:517px">TRADE SECRETS</span>
    <span class="nav-link" style="left:670px">CONTACT</span>
  </nav>
  <div class="abs account"><span>▢ CART</span><span>◯ LOG IN</span></div>

  <div class="abs eyebrow hero-eyebrow"><span class="num">01</span><span class="rule"></span><span>BEST SERVICE &amp; PRICE | HASSLE FREE | AUSTRALIA WIDE</span></div>
  <h1 class="abs hero-title">1000's of Skips at Your Finger Tips</h1>
  <div class="abs search hero-search"><div class="field">Enter Postcode or Suburb</div><div class="btn">Search</div></div>

  <div class="abs audience" style="left:900px;top:291px">Renovator</div>
  <div class="abs audience" style="left:831px;top:360px">Trade</div>
  <div class="abs audience" style="left:762px;top:429px">Builder</div>
  <div class="abs audience" style="left:693px;top:498px">National</div>
  <div class="abs audience" style="left:631px;top:565px">Corporator</div>

  <!-- advantages -->
  <div class="abs eyebrow section-eyebrow" style="left:99px;top:712px"><span class="num">02</span><span class="rule"></span><span>ADVANTAGES</span></div>
  <h2 class="abs section-title" style="left:99px;top:738px">As Easy As 1, 2, 3...</h2>

  <div class="abs band"></div>

  <div class="abs card" style="left:101px">
    <div class="art" role="img" aria-label="Illustration of a laptop with a chat bubble"></div>
    <h3>Simple, Easy Booking</h3>
    <p>Call 1800 555 019 or click here to get started with your instant quote</p>
  </div>
  <div class="abs card" style="left:448px">
    <div class="art" role="img" aria-label="Illustration of an envelope, phone and calendar"></div>
    <h3>Instant Confirmation</h3>
    <p>Receive your booking details and a 30 minute courtesy call before drop off</p>
  </div>
  <div class="abs card" style="left:796px">
    <div class="art" role="img" aria-label="Illustration of an envelope, phone and calendar"></div>
    <h3>Gone When Your Ready!</h3>
    <p>Let us know and your bin will be gone within 24hrs</p>
  </div>

  <!-- reviews -->
  <div class="abs eyebrow" style="left:99px;top:1286px"><span class="num" style="color:#9fb8d0">03</span><span class="rule"></span><span>REVIEWS</span></div>
  <h2 class="abs section-title reviews-title" style="left:99px;top:1313px">Five star service</h2>
  <div class="abs arrow" style="left:1006px">←</div>
  <div class="abs arrow" style="left:1052px">→</div>
  <div class="abs dots"><i></i><i></i><i></i><i></i><i></i></div>

  <div class="abs review" style="left:71px">
    <span class="quote">“</span>
    <div class="head"><span class="name">Priya</span><span class="date">December 29, 2018</span><span class="stars">★★★★★</span></div>
    <p>Easy to book through the website and great to have live chat facility. Bin was delivered as organised and all went well. Would use again.</p>
  </div>
  <div class="abs review" style="left:446px">
    <span class="quote">“</span>
    <div class="head"><span class="name">Priya</span><span class="date">December 29, 2018</span><span class="stars">★★★★★</span></div>
    <p>Easy to book through the website and great to have live chat facility. Bin was delivered as organised and all went well. Would use again.</p>
  </div>
  <div class="abs review" style="left:835px">
    <span class="quote">“</span>
    <div class="head"><span class="name">Priya</span><span class="date">December 29, 2018</span><span class="stars">★★★★★</span></div>
    <p>Easy to book through the website and great to have live chat facility. Bin was delivered as organised and all went well. Would use again.</p>
  </div>

  <!-- features -->
  <div class="abs eyebrow section-eyebrow" style="left:87px;top:1804px"><span class="num">04</span><span class="rule"></span><span>ADVANTAGES</span></div>
  <h2 class="abs section-title" style="left:87px;top:1830px">Five star service</h2>

  <svg class="abs" style="left:0;top:1840px" width="1200" height="700" viewBox="0 1840 1200 700">
    <defs>
      <linearGradient id="coreGrad" x1="0" y1="0" x2="0" y2="1">
        <stop offset="0" stop-color="#129a7c"/>
        <stop offset=".5" stop-color="#1b4f95"/>
        <stop offset="1" stop-color="#2a16ad"/>
      </linearGradient>
      <linearGradient id="iconGrad" x1="0" y1="0" x2="1" y2="1">
        <stop offset="0" stop-color="#10937a"/>
        <stop offset="1" stop-color="#2b1aa8"/>
      </linearGradient>
      <filter id="glow" x="-30%" y="-30%" width="160%" height="160%"><feGaussianBlur stdDeviation="18"/></filter>
    </defs>
    <polygon points="357,1888 623,1888 812,2077 812,2293 623,2482 357,2482 168,2293 168,2077" fill="none" stroke="#ececf2" stroke-width="2"/>
    <circle cx="278" cy="1980" r="9" fill="#f6c500"/>
    <circle cx="278" cy="2383" r="9" fill="#f6c500"/>
    <polygon points="404,1978 576,1978 697,2099 697,2271 576,2392 404,2392 283,2271 283,2099" fill="#5a3cf0" opacity=".5" filter="url(#glow)"/>
    <polygon points="404,1978 576,1978 697,2099 697,2271 576,2392 404,2392 283,2271 283,2099" fill="url(#coreGrad)" role="img" aria-label="Wireframe illustration of a skip bin"/>

    <g transform="translate(490,1890)">
      <polygon points="-13,-32 13,-32 32,-13 32,13 13,32 -13,32 -32,13 -32,-13" fill="url(#iconGrad)"/>
      <text x="0" y="8" text-anchor="middle" font-family="Ubuntu, sans-serif" font-size="24" font-weight="700" fill="#fff">$</text>
    </g>
    <g transform="translate(674,1992)">
      <polygon points="-13,-32 13,-32 32,-13 32,13 13,32 -13,32 -32,13 -32,-13" fill="url(#iconGrad)"/>
      <circle r="17" fill="none" stroke="#fff" stroke-width="2.5"/>
      <text x="0" y="6" text-anchor="middle" font-family="Ubuntu, sans-serif" font-size="15" font-weight="700" fill="#fff">24</text>
    </g>
    <g transform="translate(766,2180)">
      <polygon points="-13,-32 13,-32 32,-13 32,13 13,32 -13,32 -32,13 -32,-13" fill="url(#iconGrad)"/>
      <path d="M0,18 C-6,8 -12,2 -12,-5 A12,12 0 0 1 12,-5 C12,2 6,8 0,18 Z" fill="#fff"/>
      <circle cy="-5" r="4.5" fill="#1b4f95"/>
    </g>
    <g transform="translate(683,2376)">
      <polygon points="-13,-32 13,-32 32,-13 32,13 13,32 -13,32 -32,13 -32,-13" fill="url(#iconGrad)"/>
      <path d="M-13,1 L-4,10 L14,-9" fill="none" stroke="#fff" stroke-width="4" stroke-linecap="round" stroke-linejoin="round"/>
    </g>
  </svg>

  <div class="abs feature" style="left:552px;top:1855px;width:335px">
    <h3>Best Pricing</h3>
    <p>We've done the hard work behind the scenes, so with one click you have your best priced, local skip</p>
  </div>
  <div class="abs feature" style="left:736px;top:1968px;width:315px">
    <h3>Service Guaranteed</h3>
    <p>Want to speak to someone when it suits you? We answer the phones and return calls from 7.30am to</p>
  </div>
  <div class="abs feature" style="left:826px;top:2156px;width:335px">
    <h3>Any Bin, Anytime, Anywhere</h3>
    <p>We connect you with local companies Australia wide; for faster response times, less km's and emissions, greater reliability and lower prices</p>
  </div>
  <div class="abs feature" style="left:731px;top:2349px;width:360px">
    <h3>First Class Supply Partners</h3>
    <p>Our local supply partners are the best in the business and share our passion for making you happy</p>
  </div>

  <!-- ready to go -->
  <div class="abs map" role="img" aria-label="Map of Australia with state borders"></div>
  <div class="abs ready-eyebrow">CALL US 7 DAYS A WEEK 7.30AM TO 6PM</div>
  <h2 class="abs ready-title">We're ready to go!</h2>
  <div class="abs search ready-search"><div class="field">Enter Postcode or Suburb</div><div class="btn">Search</div></div>

  <!-- footer -->
  <footer class="abs footer">
    <div class="abs foot-col" style="left:87px">
      <h4>Tumble Crate Rentals Oz - Australia Wide</h4>
      <ul><li>Sydney</li><li>Melbourne</li><li>Brisbane</li><li>Perth</li><li>Adelaide</li><li>Canberra</li></ul>
    </div>
    <div class="abs foot-col" style="left:391px">
      <h4>Learn More</h4>
      <ul><li>Waste Types</li><li>Skip Bin Sizes</li><li>Refund Policy</li><li>Pay Later with</li><li>SplitPay</li><li>FAQ</li><li>Privacy</li></ul>
    </div>
    <div class="abs foot-col" style="left:697px">
      <h4>Latest industry news</h4>
      <p>Sign up for the latest news, offers from TUMBLE CRATE RENTALS OZ</p>
    </div>
    <div class="abs subscribe"><div class="field">Your E-mail</div><div class="btn">Subscribe</div></div>
    <div class="abs copyright">Copyright © 2019, TUMBLE CRATE RENTALS OZ. Powered by Crateworks</div>
  </footer>

</div>
</body>
</html>
```